Meadow Lantern Equine Refuge - Sponsorship Flyer

We require an A4 trifold flyer. Our colours are orange, black and white.
At The Meadow Lantern Equine Refuge, we have a number of our animals available for Sponsorship. The majority are horses or ponies reflecting our focus however from time to time other animals in need find the peace of our Sanctuary.

Your sponsorship donation helps with the cost of care for horses requiring long-term rehabilitation including ongoing vet care etc as more often than not, the horse will have arrived in poor condition.

For those horses that are unsound or aged, (but with quality of life) and therefore not suited for adoption, are allowed to live out their days here at the Sanctuary.

As a DGR* charity all donations over $2 are tax deductible.

We have two different sponsorship types…Guardians of MLER and Friends of MLER

Target Market(s)

Horse Lovers

Industry/Entity Type

Rescue

Font styles to use
Serif

Colors
EE7325
F08F49
F5BC92
FAE3D3
FDF4ED

Requirements
Must have
• GUARDIANS of MLER Store/SPONSORSHIP/GUARDIANS of MLER Our Guardian sponsors choose to be with us for the long term. Their regular donation helps cover the monthly costs involved with caring for our residents. We like to think of these special folk as Guardian Angels. Their generosity allows us to keep so many safe from harm in this magical place. Guardian Sponsors receive a personalised e-certificate as well as a six-monthly update. We also invite our Guardians to contact us to organise a visit to the Sanctuary at a mutually convenient time. Here, you can meet the horse or pony that has captured your heart. Sponsorship costs vary from $15 – $25 per week depending on the animal and its needs.
Should not have
• External sourced photos

```html
<!DOCTYPE html>
<html lang="en">
<head>
<meta charset="utf-8">
<title>Meadow Lantern Equine Refuge – Sponsorship Flyer</title>
<link rel="stylesheet" href="https://fonts.googleapis.com/css2?family=Cinzel:wght@600;700&family=Marcellus&family=Montserrat:wght@400;500&family=Poppins:wght@500;600&display=swap">
<style>
  :root {
    --orange: #EE7325;
    --orange-soft: #F08F49;
    --peach: #F5BC92;
    --cream: #FAE3D3;
    --paper: #FDF4ED;
    --ink: #1c1410;
    --white: #ffffff;
    --stage: #f6efe9;
  }
  * { box-sizing: border-box; margin: 0; padding: 0; }
  html, body { width: 1200px; height: 675px; overflow: hidden; }
  body { background: var(--stage); position: relative; font-family: "Montserrat", sans-serif; }

  .flyer {
    position: absolute; left: 150px; top: 20px;
    width: 900px; height: 635px;
    display: flex;
  }
  .panel { position: relative; width: 300px; height: 100%; overflow: hidden; }
  .panel--cream { background: var(--cream); }
  .panel--orange { background: var(--orange); }

  /* Cover panel */
  .brand {
    position: absolute; top: 24px; left: 0; right: 0;
    display: flex; justify-content: center; align-items: center; gap: 8px;
  }
  .brand__mark { width: 26px; height: 26px; background: var(--orange); }
  .brand__name {
    font-family: "Cinzel", serif; font-weight: 700; color: var(--orange);
    font-size: 15px; line-height: 1.05;
  }
  .tagline {
    position: absolute; top: 118px; left: 0; right: 0; text-align: center;
    font-family: "Marcellus", serif; font-size: 26px; line-height: 1.1;
  }
  .tagline__first { color: var(--ink); display: block; }
  .tagline__second { color: var(--orange); display: block; }
  .cover-photo {
    position: absolute; left: 21px; top: 195px; width: 258px; height: 335px;
    background: linear-gradient(160deg, #4f6a3c 0%, #6d6a5c 45%, #8f8a85 70%, #6b4a3a 100%);
  }
  .cover-title {
    position: absolute; top: 558px; left: 0; right: 0; text-align: center;
    font-family: "Cinzel", serif; font-weight: 700; color: var(--orange); font-size: 19px;
  }
  .cover-cta {
    position: absolute; top: 586px; left: 0; right: 0; text-align: center;
    font-family: "Cinzel", serif; font-weight: 700; color: var(--ink); font-size: 14px;
  }

  /* Middle panel */
  .angel-title {
    position: absolute; top: 46px; left: 0; right: 0; text-align: center;
    font-family: "Cinzel", serif; font-weight: 600; color: var(--white); font-size: 20px; letter-spacing: 0.5px;
  }
  .angel-text {
    position: absolute; top: 82px; left: 20px; right: 20px; text-align: center;
    color: var(--white); font-size: 9.5px; line-height: 1.2;
  }
  .angel-band {
    position: absolute; top: 164px; left: 0; right: 0; height: 18px;
    background: var(--cream); color: var(--orange);
    font-family: "Poppins", sans-serif; font-weight: 600; font-size: 11px;
    text-align: center; line-height: 18px;
  }
  .snapshot {
    position: absolute; background: var(--cream); padding: 7px; border-radius: 6px;
  }
  .snapshot__photo { width: 100%; height: 100%; border-radius: 2px; }
  .snapshot__tape {
    position: absolute; width: 46px; height: 10px; background: rgba(250, 227, 211, 0.85);
  }
  .snapshot--one { left: 78px; top: 196px; width: 186px; height: 140px; transform: rotate(-9deg); }
  .snapshot--one .snapshot__photo { background: linear-gradient(120deg, #5b3a2a 0%, #7a6a5e 45%, #dedad5 70%, #9aa3a8 100%); }
  .snapshot--two { left: 28px; top: 326px; width: 145px; height: 130px; }
  .snapshot--two .snapshot__photo { background: linear-gradient(135deg, #c2455a 0%, #2a2a30 50%, #3d6ea0 100%); }
  .snapshot--three { left: 44px; top: 474px; width: 200px; height: 128px; transform: rotate(12deg); }
  .snapshot--three .snapshot__photo { background: linear-gradient(160deg, #c9cfc3 0%, #7a4a2c 45%, #4f6a34 100%); }
  .tape--tl { left: -20px; top: 2px; transform: rotate(-40deg); }
  .tape--br { right: -20px; bottom: 2px; transform: rotate(-40deg); }
  .tape--tr { right: -18px; top: 2px; transform: rotate(40deg); }
  .tape--bl { left: -18px; bottom: 2px; transform: rotate(40deg); }

  /* Info panel */
  .section-title {
    position: absolute; left: 0; right: 0; text-align: center;
    font-family: "Cinzel", serif; font-weight: 700; color: var(--orange);
  }
  .why-title { top: 47px; font-size: 15px; }
  .why-box {
    position: absolute; left: 21px; top: 80px; width: 261px; height: 135px;
    border: 1px solid var(--orange); border-radius: 2px; padding: 7px 3px;
    color: var(--orange); font-size: 9.6px; line-height: 1.2; text-align: justify;
  }
  .why-box p + p { margin-top: 12px; }
  .help-title { top: 253px; font-size: 18px; }
  .types-title { top: 350px; font-size: 18px; }
  .button-row {
    position: absolute; left: 22px; width: 259px; height: 40px;
    display: flex; gap: 6px;
  }
  .button-row--help { top: 279px; }
  .button-row--types { top: 376px; }
  .pill {
    flex: 1; background: var(--orange); color: var(--white);
    font-family: "Poppins", sans-serif; font-weight: 600; font-size: 10px; line-height: 1.15;
    display: flex; align-items: center; justify-content: center; text-align: center;
  }
  .contact-title {
    position: absolute; top: 483px; left: 0; right: 0; text-align: center;
    font-family: "Cinzel", serif; font-weight: 700; color: var(--ink); font-size: 14px;
  }
  .contact-block {
    position: absolute; left: 0; right: 0; text-align: center;
    color: var(--ink); font-size: 9.6px; line-height: 1.2;
  }
  .contact-address { top: 516px; }
  .contact-phone { top: 551px; }
  .contact-email { top: 586px; }
</style>
</head>
<body>
<main class="flyer">

  <section class="panel panel--cream cover">
    <div class="brand">
      <span class="brand__mark"></span>
      <span class="brand__name">Meadow Lantern<br>Equine Refuge</span>
    </div>
    <h2 class="tagline">
      <span class="tagline__first">Sponsor a Life</span>
      <span class="tagline__second">Support a Soul</span>
    </h2>
    <div class="cover-photo" role="img" aria-label="Photo of a grey donkey mare and her foal beside a tree trunk"></div>
    <h1 class="cover-title">THE GUARDIANS OF MLER</h1>
    <p class="cover-cta">JOIN TODAY</p>
  </section>

  <section class="panel panel--orange guardian">
    <h2 class="angel-title">BE A GUARDIAN ANGEL</h2>
    <p class="angel-text">Sponsorship costs vary from $15 – $25 per week<br>depending on the animal and its needs.</p>
    <p class="angel-band">Ready to change a life?</p>

    <figure class="snapshot snapshot--one">
      <div class="snapshot__photo" role="img" aria-label="Photo of a bay horse and a grey horse greeting each other"></div>
      <span class="snapshot__tape tape--tl"></span>
      <span class="snapshot__tape tape--br"></span>
    </figure>
    <figure class="snapshot snapshot--two">
      <div class="snapshot__photo" role="img" aria-label="Photo of a woman hugging a dark horse in front of autumn foliage"></div>
      <span class="snapshot__tape tape--tl"></span>
      <span class="snapshot__tape tape--br"></span>
    </figure>
    <figure class="snapshot snapshot--three">
      <div class="snapshot__photo" role="img" aria-label="Photo of two bay horses nuzzling in a paddock"></div>
      <span class="snapshot__tape tape--tr"></span>
      <span class="snapshot__tape tape--bl"></span>
    </figure>
  </section>

  <section class="panel panel--cream info">
    <h2 class="section-title why-title">WHY SPONSORSHIP MATTERS</h2>
    <div class="why-box">
      <p>Your donation helps care for horses needing long-term rehabilitation — often arriving in poor condition, they require consistent vet care, food, and love.</p>
      <p>At Meadow Lantern Equine Refuge, we offer the opportunity to sponsor one of our long term residents. The monthly sponsorship covers their basic costs such as feed, worming and farrier visits. Contact us for more information.</p>
    </div>

    <h2 class="section-title help-title">TWO WAYS TO HELP</h2>
    <div class="button-row button-row--help">
      <span class="pill">Visit our website</span>
      <span class="pill">Choose a horse<br>Become a Guardian</span>
    </div>

    <h2 class="section-title types-title">SPONSORSHIP TYPES</h2>
    <div class="button-row button-row--types">
      <span class="pill">Guardians of MLER</span>
      <span class="pill">Friends of MLER</span>
    </div>

    <h2 class="contact-title">– CONTACT –</h2>
    <p class="contact-block contact-address">Meadow Lantern Equine Refuge<br>42 Willowbend Road, Larkfield. VIC 3999</p>
    <p class="contact-block contact-phone">Phone:<br>0400 555 019</p>
    <p class="contact-block contact-email">E-mail:<br>hello@meadowlantern.org.au</p>
  </section>

</main>
</body>
</html>
```